New Business Cards for MB&LR

We need updated business cards for a staff of 15 engineers, estimators, project managers, and sales people. We have recently begun changes to our website and marketing material to improve our look and branding. We are an established fabricator specializing in pressure vessels, tanks, and structural steel. The owners require us to use the existing logo and old english text design. Also, we prefer dark grey or mostly black cards.
Target Market(s)
Engineers, purchasing agents, estimators, and project managers of; mining companies, refineries, industrial construction professionals
Industry/Entity Type
Business
Contact Information for Business Card
Logo, phone, website, email, etc.
Look and feel

```html
<!DOCTYPE html>
<html lang="en">
<head>
<meta charset="utf-8">
<title>MB&amp;LR Business Card</title>
<link rel="stylesheet" href="https://fonts.googleapis.com/css2?family=Lora:wght@400;500&display=swap">
<style>
  :root {
    --backdrop: #e4e4e4;
    --card: #1b1b1b;
    --ink: #f2f2f2;
    --ink-soft: #d9d9d9;
  }
  * { margin: 0; padding: 0; box-sizing: border-box; }
  html, body {
    width: 1200px; height: 576px; overflow: hidden;
    background: var(--backdrop);
    font-family: "Lora", Georgia, serif;
    color: var(--ink);
  }
  .canvas { position: relative; width: 1200px; height: 576px; }
  .card {
    position: absolute;
    width: 482px; height: 292px;
    background: var(--card);
    border-radius: 14px;
  }
  .card--front { left: 82px; top: 138px; }
  .card--back { left: 602px; top: 138px; }

  .brand-mark {
    position: absolute;
    display: flex; align-items: center; gap: 10px;
    font-size: 30px; font-weight: 500; letter-spacing: 1px;
    color: var(--ink);
  }
  .brand-mark__dot {
    width: 16px; height: 16px; border-radius: 50%;
    background: var(--ink);
  }
  .card--front .brand-mark { left: 50%; top: 104px; transform: translateX(-50%); }
  .company-name {
    position: absolute; text-align: center;
    font-size: 17px; font-weight: 500; color: var(--ink);
  }
  .card--front .company-name { left: 0; right: 0; top: 202px; }

  .person { position: absolute; left: 28px; top: 36px; }
  .person__name { font-size: 21px; font-weight: 500; letter-spacing: 0.3px; line-height: 1.2; }
  .person__role { font-size: 10.5px; color: var(--ink-soft); }

  .address {
    position: absolute; left: 28px; top: 175px;
    font-size: 12px; line-height: 14.5px; color: var(--ink-soft);
    font-style: normal;
  }
  .contacts {
    position: absolute; left: 32px; top: 211px;
    list-style: none; font-size: 12px; color: var(--ink-soft);
  }
  .contacts li { display: flex; align-items: center; height: 15.5px; }
  .contacts svg { width: 10px; height: 10px; margin-right: 9px; fill: var(--ink-soft); }

  .card--back .brand-mark { left: 320px; top: 158px; font-size: 24px; gap: 8px; }
  .card--back .brand-mark__dot { width: 12px; height: 12px; }
  .card--back .company-name {
    left: 290px; width: 166px; top: 228px;
    font-size: 15px; line-height: 20px;
  }
</style>
</head>
<body>
<main class="canvas">
  <section class="card card--front" aria-label="Card front">
    <div class="brand-mark"><span class="brand-mark__dot"></span>MB&amp;LR</div>
    <p class="company-name">Mesa Beam &amp; Lift Rigging</p>
  </section>

  <section class="card card--back" aria-label="Card back">
    <div class="person">
      <p class="person__name">R. Calder</p>
      <p class="person__role">Director</p>
    </div>
    <address class="address">480 East 200 South<br>Granite Valley City 84120</address>
    <ul class="contacts">
      <li><svg viewBox="0 0 10 10" aria-hidden="true"><path d="M1 3.5C1 2 2.5 1 5 1s4 1 4 2.5L7.5 4 7 3H3l-.5 1zM2.5 4.5h5L8.5 9h-7z"/></svg>555-310-4477</li>
      <li><svg viewBox="0 0 10 10" aria-hidden="true"><path d="M2.5 1h5v2.5h-5zM1 4h8v3.5H7.5V6h-5v1.5H1zM3 6.5h4V9H3z"/></svg>555-310-4478</li>
      <li><svg viewBox="0 0 10 10" aria-hidden="true"><path d="M5 .8A4.2 4.2 0 1 0 5 9.2 4.2 4.2 0 0 0 5 .8zm0 1c.6.6 1 1.6 1.1 2.7H3.9C4 3.4 4.4 2.4 5 1.8zM1.9 5.5h1.9C4 6.6 4.4 7.6 5 8.2A3.2 3.2 0 0 1 1.9 5.5zm0-1A3.2 3.2 0 0 1 5 1.8c-.6.6-1 1.6-1.1 2.7zm4.2 1c-.1 1.1-.5 2.1-1.1 2.7.6-.6 1-1.6 1.1-2.7zm0 0h2A3.2 3.2 0 0 1 5 8.2c.6-.6 1-1.6 1.1-2.7zm0-1c-.1-1.1-.5-2.1-1.1-2.7a3.2 3.2 0 0 1 3.1 2.7z"/></svg>calder@mbandlr.com</li>
      <li><svg viewBox="0 0 10 10" aria-hidden="true"><path d="M1 2.5h8v5H1zm.6.4L5 5.6l3.4-2.7H1.6z"/></svg>www.mbandlr.com</li>
    </ul>
    <div class="brand-mark"><span class="brand-mark__dot"></span>MB&amp;LR</div>
    <p class="company-name">Mesa Beam &amp;<br>Lift Rigging</p>
  </section>
</main>
</body>
</html>
```